Book/Audiobook/Consulting Website

I've written a book about "LearnReach" and I need a simple website to promote and sell the book, audiobook and my consulting services.

The purpose of the site is to:

- Promote the Book and Audiobook
- Sell the Book and Audiobook (digital download)
- Market and sell my consulting that I offer to prospective online teachers as well.

I envision no more than 10 total pages on the site.

1 page as an overview of the book and a link to purchase.
1 page as an overview of the book and audiobook "package" and a link to purchase.
1 page to outline the consulting that I offer with a link to purchase.
1 page for an author bio
1 page for a "contact us" form

I will also need someone to design a simple "cover" for the book and audiobook as well, nothing fancy just basic cover art/graphic.

That's it! Please let me know if you're interested.

Thanks,

Darrel

Industry/Entity Type

Digital

```html
<!DOCTYPE html>
<html lang="en">
<head>
<meta charset="utf-8">
<title>LearnReach – Book, Audio Book &amp; Consulting</title>
<link href="https://fonts.googleapis.com/css2?family=Aldrich&family=Questrial&family=Saira+Condensed:wght@600&display=swap" rel="stylesheet">
<style>
  :root {
    --brand-blue: #0a8fd0;
    --hero-blue: #0ba6da;
    --hero-blue-deep: #0390cf;
    --accent-orange: #f0602a;
    --heading-grey: #3a3a3a;
    --body-grey: #2b2b2b;
    --footer-bg: #f3f3f3;
    --btn-orange: #f39a5c;
    --btn-green: #86c05a;
    --btn-yellow: #f7c93a;
    --white: #ffffff;
  }
  * { margin: 0; padding: 0; box-sizing: border-box; }
  html, body { width: 995px; height: 1200px; overflow: hidden; background: var(--white); }
  body { position: relative; font-family: Arial, Helvetica, sans-serif; color: var(--body-grey); }

  .site-header {
    position: absolute; left: 0; top: 0; width: 995px; height: 67px;
    background: linear-gradient(#ffffff, #e9e9e9);
  }
  .brand {
    position: absolute; left: 28px; top: 20px;
    font-family: "Aldrich", sans-serif; font-size: 33px; line-height: 40px;
    color: var(--brand-blue); letter-spacing: 0.5px; white-space: nowrap;
  }
  .main-nav { position: absolute; right: 31px; top: 37px; display: flex; gap: 29px; }
  .main-nav a {
    font-family: "Aldrich", sans-serif; font-size: 14px; color: #333;
    text-decoration: none; white-space: nowrap;
  }

  .hero {
    position: absolute; left: 0; top: 67px; width: 995px; height: 458px;
    background: linear-gradient(var(--hero-blue), var(--hero-blue-deep));
  }
  .hero-art {
    position: absolute; left: 57px; top: 22px; width: 462px; height: 398px;
    border-radius: 14px;
    background: radial-gradient(ellipse at 50% 60%, #f4f6f8 0%, #cfd6dc 45%, #4a5257 78%, rgba(74,82,87,0) 100%);
  }
  .hero-text {
    position: absolute; left: 555px; top: 83px; width: 412px;
    font-size: 14px; line-height: 16.8px; color: var(--white);
  }
  .purchase-list { position: absolute; left: 555px; top: 244px; list-style: none; }
  .purchase-btn {
    display: flex; align-items: center; gap: 10px;
    width: 288px; height: 42px; margin-bottom: 8px; padding-left: 14px;
    border-radius: 8px; border: 2px solid rgba(255,255,255,0.7);
    font-family: "Saira Condensed", sans-serif; font-weight: 600; font-size: 23px;
    color: var(--white); text-decoration: none; letter-spacing: 0.6px;
    white-space: nowrap; overflow: hidden;
  }
  .purchase-btn.book { background: linear-gradient(90deg, #f07a35, var(--btn-orange)); }
  .purchase-btn.audio { background: linear-gradient(90deg, #6cae3e, var(--btn-green)); }
  .purchase-btn.consult { background: linear-gradient(90deg, #f2b51a, var(--btn-yellow)); }
  .purchase-btn svg { flex: none; }

  .offer { position: absolute; top: 570px; }
  .offer h2 {
    font-family: "Questrial", sans-serif; font-weight: 400; font-size: 30px;
    color: var(--heading-grey); letter-spacing: -1px; line-height: 36px; white-space: nowrap;
  }
  .offer p { font-size: 12px; line-height: 14.5px; color: var(--body-grey); }
  .offer .lead-block { position: absolute; }
  .offer .lead-block p + p { margin-top: 11px; }
  .offer .wide { position: absolute; }
  .offer .links { position: absolute; font-size: 12px; line-height: 18px; }
  .offer .links a { display: block; text-decoration: none; white-space: nowrap; }
  .more-info { color: var(--accent-orange); }
  .buy-link { color: var(--brand-blue); }
  .cover-art { position: absolute; border-radius: 4px; }

  .offer-book { left: 27px; }
  .offer-book .cover-art { left: 0; top: 58px; width: 118px; height: 184px;
    background: linear-gradient(135deg, #2ea6e0, #0b74b8); }
  .offer-book .lead-block { left: 137px; top: 60px; width: 140px; }
  .offer-book .wide { left: 0; top: 273px; width: 262px; }
  .offer-book .links { left: 0; top: 363px; }

  .offer-audio { left: 361px; }
  .offer-audio .cover-art { left: 0; top: 78px; width: 128px; height: 150px;
    background: radial-gradient(circle at 45% 55%, #2b7fc0, #b0392e 70%, rgba(176,57,46,0) 100%); border-radius: 20px; }
  .offer-audio .lead-block { left: 154px; top: 58px; width: 140px; }
  .offer-audio .wide { left: 0; top: 273px; width: 262px; }
  .offer-audio .links { left: 2px; top: 363px; }

  .offer-consult { left: 720px; }
  .offer-consult .lead-block { left: 3px; top: 48px; width: 252px; }
  .offer-consult .lead-block p + p { margin-top: 15px; }
  .offer-consult .links { left: 2px; top: 233px; }

  .site-footer {
    position: absolute; left: 0; top: 1025px; width: 995px; height: 175px;
    background: var(--footer-bg);
  }
  .social { position: absolute; left: 405px; top: 33px; display: flex; gap: 8px; list-style: none; }
  .social li { width: 30px; height: 30px; background: var(--brand-blue); }
  .footer-rule { position: absolute; left: 18px; top: 76px; width: 962px; border-top: 1px dotted #bbb; }
  .footer-nav { position: absolute; left: 0; top: 86px; width: 995px; text-align: center; font-size: 15px; color: var(--brand-blue); }
  .footer-nav a { color: var(--brand-blue); text-decoration: none; }
  .copyright { position: absolute; left: 0; top: 109px; width: 995px; text-align: center; font-size: 11px; color: #f07a35; }
</style>
</head>
<body>
  <header class="site-header">
    <div class="brand">LEARNREACH</div>
    <nav class="main-nav">
      <a href="#">HOME</a><a href="#">ABOUT</a><a href="#">BOOK</a><a href="#">AUDIOBOOK</a><a href="#">CONSULTING</a>
    </nav>
  </header>

  <section class="hero">
    <div class="hero-art" role="img" aria-label="Illustration of an open book on a tablet with colourful speech bubbles for languages, maths, reading, geography and audio"></div>
    <p class="hero-text">Lorem ipsum dolor sit amet, consectetur adipisicing elit, sed do eiusmod tempor incididunt ut labore et dolore magna aliqua. Ut enim ad minim veniam, quis nostrud exercitation ullamco laboris nisi ut aliquip ex ea commodo consequat. Duis aute irure dolor in reprehenderit in voluptate velit esse cillum dolore eu fugiat nulla pariatur. Excepteur sint occaecat cupidatat non proident, sunt in culpa qui officia deserunt mollit anim id est laborum.</p>
    <ul class="purchase-list">
      <li><a class="purchase-btn book" href="#">
        <svg width="32" height="22" viewBox="0 0 32 22"><path d="M2 3 Q9 0 16 4 Q23 0 30 3 V20 Q23 17 16 21 Q9 17 2 20 Z M16 4 V21" fill="none" stroke="#fff" stroke-width="2"/></svg>
        PURCHASE BOOK</a></li>
      <li><a class="purchase-btn audio" href="#">
        <svg width="32" height="24" viewBox="0 0 32 24"><path d="M6 16 V12 A10 10 0 0 1 26 12 V16" fill="none" stroke="#fff" stroke-width="2.5"/><rect x="4" y="14" width="6" height="9" rx="2" fill="#fff"/><rect x="22" y="14" width="6" height="9" rx="2" fill="#fff"/></svg>
        PURCHASE AUDIO BOOK</a></li>
      <li><a class="purchase-btn consult" href="#">
        <svg width="32" height="22" viewBox="0 0 32 22"><circle cx="7" cy="7" r="3" fill="#fff"/><circle cx="16" cy="6" r="3" fill="#fff"/><circle cx="25" cy="7" r="3" fill="#fff"/><rect x="1" y="12" width="30" height="9" rx="2" fill="#fff"/></svg>
        PURCHASE CONSULTING</a></li>
    </ul>
  </section>

  <section class="offer offer-book">
    <h2>THE BOOK</h2>
    <div class="cover-art" role="img" aria-label="Blue book cover illustration"></div>
    <div class="lead-block">
      <p>Lorem ipsum dolor sit amet, consectetur adipisicing elit, sed do eiusmod tempor incididunt ut labore et dolore magna aliqua. Ut enim ad minim veniam, quis laboris.</p>
      <p>Consectetur adipisicing elit, sed do eiusmod tempor incididunt ut labore et dolore magna aliqua. Ut enim ad minim</p>
    </div>
    <p class="wide">Sed ut perspiciatis, unde omnis iste natus error sit voluptatem accusantium doloremque laudantium, totam rem aperiam eaque ipsa, quae ab illo inventore veritatis et quasi architecto beatae vitae dicta sunt, explicabo.</p>
    <div class="links"><a class="more-info" href="#">more info</a><a class="buy-link" href="#">purchase book</a></div>
  </section>

  <section class="offer offer-audio">
    <h2>THE AUDIO BOOK</h2>
    <div class="cover-art" role="img" aria-label="Illustration of a stack of books with headphones"></div>
    <div class="lead-block">
      <p>Lorem ipsum dolor sit amet, consectetur adipisicing elit, sed do eiusmod tempor incididunt ut labore et dolore magna aliqua. Ut enim ad minim veniam, quis laboris.</p>
      <p>Consectetur adipisicing elit, sed do eiusmod tempor incididunt ut labore et dolore magna aliqua. Ut enim ad minim</p>
    </div>
    <p class="wide">Sed ut perspiciatis, unde omnis iste natus error sit voluptatem accusantium doloremque laudantium, totam rem aperiam eaque ipsa, quae ab illo inventore veritatis et quasi architecto beatae vitae dicta sunt, explicabo.</p>
    <div class="links"><a class="more-info" href="#">more info</a><a class="buy-link" href="#">purchase book</a></div>
  </section>

  <section class="offer offer-consult">
    <h2>CONSULTING</h2>
    <div class="lead-block">
      <p>Lorem ipsum dolor sit amet, consectetur adipisicing elit, sed do eiusmod tempor incididunt ut labore et dolore magna aliqua. Ut enim ad minim veniam, quis nostrud exercitation ullamco laboris nisi ut aliquip ex ea commodo consequat.</p>
      <p>Sed ut perspiciatis, unde omnis iste natus error sit voluptatem accusantium doloremque laudantium, totam rem aperiam eaque ipsa, quae ab illo inventore veritatis et quasi architecto beatae vitae dicta sunt, explicabo.</p>
    </div>
    <div class="links"><a class="more-info" href="#">more info</a><a class="buy-link" href="#">purchase book</a></div>
  </section>

  <footer class="site-footer">
    <ul class="social" aria-label="Social links">
      <li></li><li></li><li></li><li></li><li></li>
    </ul>
    <div class="footer-rule"></div>
    <nav class="footer-nav">
      <a href="#">Home</a> · <a href="#">About</a> · <a href="#">Book</a> · <a href="#">Audio Boook</a> · <a href="#">Consulting</a> · <a href="#">Contact</a>
    </nav>
    <p class="copyright">© Copyright 2013 LearnReach. All Rights Reserved</p>
  </footer>
</body>
</html>
```